HBL Corporate Identity

As the first stage of implementing a new corporate identity we need a logo, letterhead and business card design.

The Harbourline Residents Alliance of Australia Inc (HBL) is a non-profit, volunteer-run association representing owners of strata-titled residential developments. We provide education, information and lobbying to improve the management of apartment complexes and the lives of those living in them. We’re all about “owners helping owners”. More information on our organisation can be seen at www.hbl.org.au.

The logo will be used on our own stationery and promotional materials. It will also be provided to our sponsors for use on their collateral – as such it needs to be of a ‘standard’ size so it can be easily used in a wide of materials.

Once we have chosen the new logo and corresponding design concept we will open a new contest for a complementary layout design for our website.
Updates

Thank you to everyone who submitted designs for us. There were many really great concepts, and we appreciate the effort that everyone went to - but as you know we can only choose one.

Kind regards
Margot

Target Market(s)

The primary audience is Owners of residential apartments - both resident owners and investor owners.

Secondary audiences – current and potential sponsors; organisations providing products & services to Owners Corporations & Body Corporates

Industry/Entity Type

Non-Profit

Requirements
Must have
• The design and colours should reflect a sense of community, coupled with authority, professionalism and knowledge.

We are open to all ideas.

```html
<!DOCTYPE html>
<html lang="en">
<head>
<meta charset="utf-8">
<title>HBL Stationery</title>
<link href="https://fonts.googleapis.com/css2?family=Archivo+Black&family=Arimo:wght@400;700&family=Open+Sans:wght@400;600;700&display=swap" rel="stylesheet">
<style>
:root{
  --bg:#ece7dc;
  --paper:#ffffff;
  --ink:#111111;
  --grey:#5a5a5a;
  --muted:#a9a9a9;
  --rule:#e3e3e3;
  --navy:#4a52a3;
  --violet:#8262ad;
  --sky:#72b5e3;
  --green:#5aa752;
  --orange:#f6aa60;
  --red:#e05550;
}
*{margin:0;padding:0;box-sizing:border-box}
html,body{width:1200px;height:1123px;overflow:hidden}
body{background:var(--bg);position:relative;font-family:"Arimo",Arial,sans-serif;color:var(--ink)}
.sheet{position:absolute;background:var(--paper);box-shadow:0 2px 10px rgba(0,0,0,.18)}

/* logo panel */
.logo-panel{left:30px;top:195px;width:400px;height:156px;display:flex;align-items:center;gap:22px;padding-left:34px}
.brand-dot{width:34px;height:34px;border-radius:50%;background:var(--navy);flex:none}
.brand-name{font-family:"Archivo Black",Arial,sans-serif;font-size:25px;line-height:1.05;color:var(--ink)}

/* letterhead */
.letterhead{left:650px;top:195px;width:520px;height:735px;overflow:hidden}
.letterhead .edge{position:absolute;left:0;top:0;width:10px;height:100%;background:linear-gradient(var(--navy) 0 32%,var(--paper) 32% 70%,var(--orange) 70% 82%,var(--red) 82% 100%)}
.letterhead .head-brand{position:absolute;left:40px;top:42px;display:flex;align-items:center;gap:12px}
.letterhead .brand-dot{width:26px;height:26px}
.letterhead .head-name{font-family:"Arimo",Arial,sans-serif;font-weight:700;font-variant:small-caps;font-size:15px;line-height:1.1;color:var(--grey)}
.letterhead .contact{position:absolute;right:34px;top:34px;font-size:9.5px;line-height:1.45;color:var(--muted)}
.letterhead .contact b{font-weight:700}
.letterhead .rule{position:absolute;left:40px;right:34px;top:112px;height:1px;background:var(--rule)}
.letterhead .watermark{position:absolute;left:170px;top:250px;width:320px;height:440px;border-radius:50%;
  background:radial-gradient(ellipse at center,rgba(130,98,173,.16),rgba(114,181,227,.12) 45%,rgba(246,170,96,.08) 65%,rgba(255,255,255,0) 72%)}

/* envelope */
.envelope{left:30px;top:380px;width:590px;height:300px;overflow:hidden}
.envelope .side-field{position:absolute;left:0;top:0;width:62px;height:100%;
  background:linear-gradient(180deg,var(--red),var(--orange) 25%,var(--green) 45%,var(--sky) 65%,var(--violet) 85%,var(--navy))}
.envelope .base{position:absolute;left:0;bottom:0;width:100%;height:8px;display:flex}
.envelope .base span{flex:1}
.envelope .env-brand{position:absolute;left:90px;top:30px;display:flex;align-items:center;gap:12px}
.envelope .brand-dot{width:28px;height:28px}
.envelope .env-name{font-weight:700;font-size:14px;line-height:1.15;color:var(--grey)}
.envelope .return{position:absolute;left:92px;bottom:34px;font-size:12px;line-height:1.55;color:var(--grey)}
.envelope .return .addr{font-weight:700;margin-bottom:4px}
.envelope .return .row{display:flex;align-items:center;gap:7px}
.envelope .return svg{width:11px;height:11px;flex:none}

/* business cards */
.card{top:720px;width:285px;height:185px;overflow:hidden}
.card-front{left:30px}
.card-front .stripe-field{position:absolute;right:0;top:0;width:110px;height:100%;
  background:linear-gradient(160deg,var(--sky),var(--navy) 30%,var(--green) 55%,var(--orange) 75%,var(--red))}
.card-front .front-brand{position:absolute;left:24px;top:64px;display:flex;align-items:center;gap:10px}
.card-front .brand-dot{width:24px;height:24px}
.card-front .front-name{font-weight:700;font-variant:small-caps;font-size:14px;line-height:1.1;color:var(--grey)}
.card-back{left:335px}
.card-back .stripe-field{position:absolute;left:0;top:0;width:70px;height:100%;
  background:linear-gradient(180deg,var(--red),var(--green) 20%,var(--sky) 40%,var(--navy) 60%,var(--violet) 80%,var(--sky))}
.card-back .person{position:absolute;left:84px;top:50px;font-family:"Open Sans",Arial,sans-serif}
.card-back .person-name{font-weight:700;font-size:13px;color:#444}
.card-back .person-role{font-size:9.5px;color:#333;margin-top:4px}
.card-back .details{position:absolute;left:84px;top:98px;font-size:8.6px;line-height:1.45;color:#333}
.card-back .details b{font-weight:700}
</style>
</head>
<body>

<section class="sheet logo-panel" aria-label="Logo">
  <span class="brand-dot"></span>
  <p class="brand-name">Harbourline<br>Residents<br>Alliance</p>
</section>

<section class="sheet letterhead" aria-label="Letterhead">
  <div class="edge"></div>
  <div class="head-brand">
    <span class="brand-dot"></span>
    <p class="head-name">Harbourline<br>Residents<br>Alliance</p>
  </div>
  <address class="contact">
    <b>A:</b> 1234 XXX st. #A-1234 Any City, xx 12345<br>
    <b>P:</b> (555) 555-5555 ext. 1234<br>
    <b>F:</b> (555) 555-4321<br>
    <b>E:</b> xxxx@xxxxx.com<br>
    <b>W:</b> www.hbl.org.au
  </address>
  <div class="rule"></div>
  <div class="watermark" role="img" aria-label="Faint multicoloured background decoration"></div>
</section>

<section class="sheet envelope" aria-label="Envelope">
  <div class="side-field" role="img" aria-label="Multicoloured stripe decoration"></div>
  <div class="env-brand">
    <span class="brand-dot"></span>
    <p class="env-name">Harbourline<br>Residents Alliance</p>
  </div>
  <address class="return">
    <p class="addr">1234 XXX St. #A-1234<br>Any City, XX 12345</p>
    <p class="row"><svg viewBox="0 0 12 12"><path d="M3 1l2 3-1 1.2c.6 1.4 1.4 2.2 2.8 2.8L8 7l3 2-1 2C5 11 1 7 1 2z" fill="none" stroke="#5a5a5a" stroke-width="1"/></svg>(555) 555-1234</p>
    <p class="row"><svg viewBox="0 0 12 12"><rect x="1" y="2.5" width="10" height="7" fill="none" stroke="#5a5a5a"/><path d="M1 2.5l5 4 5-4" fill="none" stroke="#5a5a5a"/></svg>xxx@xxxxx.com</p>
    <p class="row"><svg viewBox="0 0 12 12"><circle cx="6" cy="6" r="4.8" fill="none" stroke="#5a5a5a"/><path d="M1.2 6h9.6M6 1.2c2 2.4 2 7.2 0 9.6M6 1.2c-2 2.4-2 7.2 0 9.6" fill="none" stroke="#5a5a5a" stroke-width=".8"/></svg>www.hbl.org.au</p>
  </address>
  <div class="base">
    <span style="background:var(--navy)"></span><span style="background:var(--violet)"></span><span style="background:var(--sky)"></span><span style="background:var(--green)"></span><span style="background:var(--orange)"></span><span style="background:var(--red)"></span>
  </div>
</section>

<section class="sheet card card-front" aria-label="Business card front">
  <div class="front-brand">
    <span class="brand-dot"></span>
    <p class="front-name">Harbourline<br>Residents<br>Alliance</p>
  </div>
  <div class="stripe-field" role="img" aria-label="Multicoloured diagonal stripe decoration"></div>
</section>

<section class="sheet card card-back" aria-label="Business card back">
  <div class="stripe-field" role="img" aria-label="Multicoloured horizontal stripe decoration"></div>
  <div class="person">
    <p class="person-name">Lorem Ipsum</p>
    <p class="person-role">Managing Director</p>
  </div>
  <address class="details">
    <b>A:</b> 1234 XXX st. #A-1234, Any City, xx 12345<br>
    <b>P:</b> (555) 555-5555 ext. 1234<br>
    <b>F:</b> (555) 555-4321<br>
    <b>E:</b> xxxx@xxxx.com<br>
    <b>W:</b> www.hbl.org.au
  </address>
</section>

</body>
</html>
```